Property investment company needs a letterhead design!

We are a new residential and commercial property investment company. Name of the company is Morvesta Group, LLC. We have a new logo and now we need letterhead! We prefer to have a professional and upscale appearance. We don't have any fixed requirements, so be creative! Thank you for considering this project. We are so excited to see what happens!

Target Market(s)

Professional

Industry/Entity Type

Real Estate Development

```html
<!DOCTYPE html>
<html lang="en">
<head>
<meta charset="utf-8">
<title>Morvesta Group, LLC — Letterhead</title>
<link href="https://fonts.googleapis.com/css2?family=Open+Sans:wght@400;700;800&family=Great+Vibes&display=swap" rel="stylesheet">
<style>
  :root{
    --navy:#0b2140;
    --sky:#00aeef;
    --ink:#1d1d1f;
    --paper:#ffffff;
    --backdrop:#dddee4;
  }
  *{margin:0;padding:0;box-sizing:border-box}
  html,body{width:1200px;height:899px;overflow:hidden;background:var(--backdrop)}
  body{font-family:"Open Sans",Arial,sans-serif;position:relative}
  .letterhead{
    position:absolute;left:295px;top:19px;width:610px;height:860px;
    background:var(--paper);box-shadow:0 4px 14px rgba(0,0,0,.18);overflow:hidden;
  }
  .letterhead-frame{position:absolute;inset:0;width:100%;height:100%}
  .brand{
    position:absolute;left:36px;top:106px;display:flex;align-items:center;gap:10px;
  }
  .brand-dot{width:26px;height:26px;border-radius:50%;background:var(--sky)}
  .brand-name{font-weight:800;font-size:22px;color:var(--navy);letter-spacing:.3px}
  .headline{
    position:absolute;left:35px;top:214px;font-weight:800;font-size:35px;color:var(--navy);
    letter-spacing:.5px;
  }
  .body-copy{
    position:absolute;left:37px;width:537px;font-size:12px;line-height:16.8px;color:var(--ink);
    text-align:justify;
  }
  .p1{top:279px}
  .p2{top:426px}
  .p3{top:603px}
  .sign-off{position:absolute;right:36px;top:706px;text-align:right;color:var(--navy)}
  .sign-script{font-family:"Great Vibes",cursive;font-size:20px;line-height:24px}
  .sign-label{font-size:25px;line-height:30px}
  .contact-bar{
    position:absolute;top:801px;left:0;right:0;height:59px;color:#fff;font-size:12px;line-height:16.5px;
  }
  .contact-item{position:absolute;display:flex;align-items:center;gap:6px}
  .contact-item svg{width:10px;height:10px;flex:none;fill:var(--sky)}
  .address{left:155px;top:12px;align-items:flex-start}
  .address svg{margin-top:3px}
  .online{left:319px;top:12px;flex-direction:column;align-items:flex-start;gap:0}
  .online .row{display:flex;align-items:center;gap:6px}
  .phone{left:499px;top:21px}
  .divider{position:absolute;top:15px;width:1px;height:30px;background:#fff}
  .d1{left:307px}
  .d2{left:487px}
</style>
</head>
<body>
<main class="letterhead">
  <svg class="letterhead-frame" viewBox="572 144 856 1206" preserveAspectRatio="none" aria-hidden="true">
    <!-- top band -->
    <polygon points="572,144 1036,144 1014,170 572,170" fill="var(--navy)"/>
    <polyline points="572,181 994,181 1004,171" fill="none" stroke="var(--sky)" stroke-width="4"/>
    <!-- top right chevron -->
    <polygon points="1090,144 1386,144 1237,292" fill="var(--sky)"/>
    <polyline points="1050,144 1133,227 1153,207" fill="none" stroke="var(--navy)" stroke-width="4"/>
    <polyline points="1068,144 1213,288 1223,278" fill="none" stroke="var(--sky)" stroke-width="4"/>
    <polyline points="1412,144 1283,262 1293,270" fill="none" stroke="var(--sky)" stroke-width="4"/>
    <polyline points="1428,160 1296,292 1268,264" fill="none" stroke="var(--navy)" stroke-width="4"/>
    <!-- bottom left stripes -->
    <polygon points="572,1168 720,1350 572,1350" fill="var(--sky)"/>
    <polygon points="628,1234 678,1234 770,1350 720,1350" fill="var(--navy)"/>
    <polygon points="695,1256 738,1256 808,1350 768,1350" fill="var(--sky)"/>
    <polyline points="592,1192 653,1192 708,1256" fill="none" stroke="var(--navy)" stroke-width="4"/>
    <polyline points="684,1228 735,1228 768,1268" fill="none" stroke="var(--sky)" stroke-width="4"/>
    <!-- footer band -->
    <polygon points="748,1268 1428,1268 1428,1350 808,1350" fill="var(--navy)"/>
  </svg>

  <div class="brand">
    <span class="brand-dot"></span>
    <span class="brand-name">Morvesta Group, LLC</span>
  </div>

  <h1 class="headline">HEAD LINE</h1>

  <p class="body-copy p1">Lorem Ipsum is simply dummy text of the printing and typesetting industry. Lorem Ipsum has been the industry's standard dummy text ever since the 1500s, when an unknown printer took a galley of type and scrambled it to make a type specimen book. It has survived not only five centuries, but also the leap into electronic typesetting, remaining essentially unchanged. It was popularised in the 1960s with the release of Typeline sheets containing Lorem Ipsum passages, and more recently with desktop publishing software like Quillset Composer including versions of Lorem Ipsum.</p>

  <p class="body-copy p2">Contrary to popular belief, Lorem Ipsum is not simply random text. It has roots in a piece of classical Latin literature from 45 BC, making it over 2000 years old. Edwin Harlowe, a Latin professor at Brookmere College in Virginia, looked up one of the more obscure Latin words, consectetur, from a Lorem Ipsum passage, and going through the cites of the word in classical literature, discovered the undoubtable source. Lorem Ipsum comes from sections 1.10.32 and 1.10.33 of "de Finibus Bonorum et Malorum" (The Extremes of Good and Evil) by Varennus, written in 45 BC. This book is a treatise on the theory of ethics, very popular during the Renaissance. The first line of Lorem Ipsum, "Lorem ipsum dolor sit amet..", comes from a line in section 1.10.32.</p>

  <p class="body-copy p3">There are many variations of passages of Lorem Ipsum available, but the majority have suffered alteration in some form, by injected humour, or randomised words which don't look even slightly believable.</p>

  <div class="sign-off">
    <div class="sign-script">Lorem Ipsum</div>
    <div class="sign-label">Signature</div>
  </div>

  <footer class="contact-bar">
    <div class="contact-item address">
      <svg viewBox="0 0 10 10"><path d="M5 0a3.6 3.6 0 0 0-3.6 3.6C1.4 6.3 5 10 5 10s3.6-3.7 3.6-6.4A3.6 3.6 0 0 0 5 0zm0 5a1.4 1.4 0 1 1 0-2.8A1.4 1.4 0 0 1 5 5z"/></svg>
      <span>1480 N. Alder Ave.<br>Pine Hollow, MI 49611</span>
    </div>
    <span class="divider d1"></span>
    <div class="contact-item online">
      <span class="row"><svg viewBox="0 0 10 10"><path d="M5 0a5 5 0 1 0 0 10A5 5 0 0 0 5 0zm0 1.1c.5.5.9 1.4 1 2.4H4c.1-1 .5-1.9 1-2.4zM3 3.5H1.3A4 4 0 0 1 3.6 1.3 5 5 0 0 0 3 3.5zm0 1v1H1.1a4 4 0 0 1 0-1zm1 0h2v1H4zm3 0h1.9a4 4 0 0 1 0 1H7zm0-1a5 5 0 0 0-.6-2.2 4 4 0 0 1 2.3 2.2zM3 6.5a5 5 0 0 0 .6 2.2A4 4 0 0 1 1.3 6.5zm1 0h2c-.1 1-.5 1.9-1 2.4-.5-.5-.9-1.4-1-2.4zm3 0h1.7a4 4 0 0 1-2.3 2.2A5 5 0 0 0 7 6.5z"/></svg>www.morvestallc.com</span>
      <span class="row"><svg viewBox="0 0 10 10"><path d="M0 2h10v6H0zm1 1v.3l4 2.5 4-2.5V3z"/></svg>MorvestaLLC@mailbox.com</span>
    </div>
    <span class="divider d2"></span>
    <div class="contact-item phone">
      <svg viewBox="0 0 10 10"><path d="M2.2 0.5l1.6 1.9-.9 1.2c.6 1.3 1.6 2.3 2.9 2.9l1.2-.9 1.9 1.6-1 1.8C4.4 9 1 5.6.4 2z"/></svg>
      <span>7895-210-384</span>
    </div>
  </footer>
</main>
</body>
</html>
```